KRT Brochure

Brochure to communicate the concept and financial value of the company and its services to an executive audience. Attachments have detailed copy I want to use.
Updates

I have added a file that includes high res versions of company logo.

Reason: I am worried that the feedback and creation of new versions may take too long to complete by Sunday! This deadline will NOT move again though.

Target Market(s)

Chief Financial Officers in hospitals and other health organizations

Industry/Entity Type

Financial

Requirements
Must have
• Must be a 2-sided, single page.

```html
<!DOCTYPE html>
<html lang="en">
<head>
<meta charset="utf-8">
<title>KRT Brochure – Solutions for a Stronger Bottom Line</title>
<link rel="stylesheet" href="https://fonts.googleapis.com/css2?family=Arimo:wght@400;700&display=swap">
<style>
  :root {
    --brand-blue: #2a90e6;
    --brand-green: #97d51c;
    --ink: #222222;
    --body-grey: #6a6a6a;
    --divider-grey: #8a8a8a;
    --paper: #ffffff;
  }
  * { box-sizing: border-box; margin: 0; padding: 0; }
  html, body { width: 927px; height: 1200px; overflow: hidden; background: var(--paper); }
  body { font-family: "Arimo", Arial, sans-serif; color: var(--ink); }
  .sheet { position: relative; width: 927px; height: 1200px; }

  .brand { position: absolute; left: 55px; top: 46px; display: flex; align-items: center; height: 114px; }
  .brand-square { width: 98px; height: 98px; background: var(--brand-green); border-radius: 10px; }
  .brand-rule { width: 1px; height: 114px; background: var(--divider-grey); margin: 0 12px 0 16px; }
  .brand-name { font-size: 24px; line-height: 27px; font-weight: 400; color: #3a3a3a; letter-spacing: 1px; text-transform: uppercase; }

  .headline { position: absolute; left: 62px; top: 206px; font-size: 66px; line-height: 62px; font-weight: 700; color: var(--brand-blue); letter-spacing: -0.5px; }
  .headline-bar { position: absolute; left: 55px; top: 347px; width: 715px; height: 13px; border-radius: 7px; background: var(--brand-green); }

  .service { position: absolute; border-left: 3px solid var(--brand-green); padding-left: 13px; }
  .service h2 { font-size: 38px; line-height: 40px; font-weight: 700; color: var(--brand-blue); margin: -4px 0 12px; letter-spacing: -0.3px; white-space: nowrap; }
  .service .lead { font-size: 14px; line-height: 20px; font-weight: 700; color: var(--ink); margin-bottom: 20px; }
  .service .detail { font-size: 14px; line-height: 20px; color: var(--body-grey); margin-bottom: 20px; }
  .service .detail.dark { color: #333333; }
  .service .detail b { color: var(--ink); }

  .sourcing { left: 60px; top: 428px; width: 405px; height: 225px; }
  .staffing { left: 476px; top: 428px; width: 410px; height: 200px; }
  .energy { left: 60px; top: 686px; width: 410px; height: 204px; }
  .analytics { left: 476px; top: 686px; width: 410px; height: 314px; }

  .footer { position: absolute; left: 55px; top: 1097px; width: 817px; height: 48px; border-radius: 12px; background: var(--brand-green); color: #ffffff; font-size: 14.5px; display: flex; align-items: center; padding-left: 16px; white-space: nowrap; }
</style>
</head>
<body>
<main class="sheet">
  <header class="brand">
    <div class="brand-square"></div>
    <div class="brand-rule"></div>
    <div class="brand-name">The<br>Clinical<br>Margin<br>Collective</div>
  </header>

  <h1 class="headline">Solutions for a<br>Stronger Bottom Line</h1>
  <div class="headline-bar"></div>

  <section class="service sourcing">
    <h2>Strategic Sourcing</h2>
    <p class="lead">Supplier spending often compromises 35-40% of a hospital’s operating costs. This is a significant cost reduction opportunity.</p>
    <p class="detail">Using deep subject matter expertise and a large real time database, our sourcing efforts deliver an average savings of 18%. Our team has worked with over 500 clients since 1992, with experience in over 100 spend categories. We consistently exceed GPO savings.</p>
  </section>

  <section class="service staffing">
    <h2>Surgical Staffing</h2>
    <p class="lead">Facilities often provide surgical first assistance without reimbursement. Surgeons often ask colleagues to assist in cases.</p>
    <p class="detail dark">Out “in-sourcing” program provides trained professional surgical first assistants (SFA’s) to hospitals and surgery centers to offset expenses, increase throughout, and provide the best possible support for surgeons and their patients.</p>
  </section>

  <section class="service energy">
    <h2>Energy Conservation</h2>
    <p class="lead">Hospitals are among the largest users of energy per sq ft. EPA estimates that an average of 30% of energy&nbsp; consumed by commercial buildings is wasted.</p>
    <p class="detail dark">Our engineers evaluate your facility’s mechanical systems, controls, and energy usage, identifying and implementing non-capital projects that reduce consumption and costs by 10-30%.</p>
  </section>

  <section class="service analytics">
    <h2>Revenue Analytics</h2>
    <p class="lead">Few hospitals realize the revenue-generating power of their data.</p>
    <p class="detail dark"><b>Pricing.</b> Mathematically implemented strategic pricing, optimization of price sensitive net revenue based on market position, patient mix, contracts, and your business rules.</p>
    <p class="detail dark"><b>Charge Capture.</b> Analysis of charge data vs. a repository of standards. Analysis of completeness of claims to identify and realize revenue gains.</p>
    <p class="detail dark"><b>ICD-10.</b> Analytics to identify areas of high vs. low risk and complexity, enabling better prioritization of efforts.</p>
  </section>

  <footer class="footer">www.ClinicalMarginCollective.com | info@krtpartner.net | (206) 555-0147 | Copyright 2012 KRT Partners LLC</footer>
</main>
</body>
</html>
```